Miraluna Festival Poster

I need an artsy design for a poster for Miraluna 2019. The event is October 7-12 in Historic Green Cove Springs. I will need a vector design with full bleed that will translate to 4x6 inch push cards, 11x17 inch posters, 4x4 feet posters and 4x8 feet banner. The poster and push cards need a white band at the bottom for sponsors. I have to be able to edit the text because we will need some printed posters in Spanish. I am uploading 2 previous posters so that you will see the colors I wish to use. The design must be bright and eye-catching. Thank you for your interest.

```html
<!DOCTYPE html>
<html lang="en">
<head>
<meta charset="UTF-8">
<title>Miraluna 2019 Music &amp; Arts Festival Poster</title>
<link href="https://fonts.googleapis.com/css2?family=Rubik+Dirt&family=Satisfy&family=Special+Elite&family=Oswald:wght@500&family=Lora:ital@1&display=swap" rel="stylesheet">
<style>
  :root {
    --canvas: #d9d9db;
    --ink-white: #f4f1f3;
    --plum-deep: #241423;
    --plum: #4a2a4c;
    --violet: #6c3f6f;
    --magenta: #c0457e;
    --accent-red: #e0322f;
    --sponsor-blue: #1f3f8f;
    --sponsor-grey: #4d4d55;
    --band: #ffffff;
  }
  * { box-sizing: border-box; margin: 0; padding: 0; }
  html, body { width: 1200px; height: 800px; overflow: hidden; }
  body { background: var(--canvas); position: relative; }

  .poster {
    position: absolute;
    left: 360px; top: 30px;
    width: 480px; height: 740px;
    overflow: hidden;
    background: var(--plum-deep);
  }
  .poster__photo {
    position: absolute; inset: 0 0 111px 0;
    background:
      radial-gradient(ellipse 40% 30% at 88% 58%, rgba(192,69,126,.75), transparent 70%),
      radial-gradient(ellipse 50% 40% at 70% 20%, rgba(108,63,111,.9), transparent 75%),
      radial-gradient(ellipse 35% 60% at 12% 35%, rgba(120,80,90,.55), transparent 70%),
      linear-gradient(170deg, var(--violet) 0%, var(--plum) 45%, var(--plum-deep) 100%);
  }

  .event-badge {
    position: absolute; left: 118px; top: 68px;
    width: 92px; height: 66px;
    background: var(--band);
    display: flex; align-items: center; justify-content: center;
    gap: 5px; padding: 4px;
  }
  .event-badge__dot { width: 10px; height: 10px; border-radius: 50%; background: #7cb342; flex: none; }
  .event-badge__name {
    font-family: "Oswald", sans-serif; font-weight: 500;
    font-size: 13px; line-height: 1.05; color: #3d6b2a; text-transform: uppercase;
  }

  .poster__year {
    position: absolute; left: 0; right: 0; top: 148px;
    text-align: center;
    font-family: "Rubik Dirt", sans-serif;
    font-size: 84px; color: var(--ink-white); letter-spacing: 2px;
  }
  .poster__title {
    position: absolute; left: 0; right: 0; top: 236px;
    text-align: center;
    font-family: "Satisfy", cursive;
    font-size: 108px; line-height: 1; color: var(--ink-white);
  }
  .poster__subtitle {
    position: absolute; left: 0; right: 0; top: 352px;
    text-align: center;
    font-family: "Rubik Dirt", sans-serif;
    font-size: 27px; color: var(--ink-white); letter-spacing: 1px;
  }
  .poster__details {
    position: absolute; left: 136px; top: 425px;
    font-family: "Special Elite", monospace;
    font-size: 25px; line-height: 1.42; color: var(--ink-white);
    text-transform: uppercase;
  }
  .poster__details .place { display: block; }
  .poster__details .state { display: block; padding-left: 30px; }

  .poster__visit {
    position: absolute; left: 0; right: 0; top: 596px;
    text-align: center;
    font-family: "Oswald", sans-serif; font-weight: 500;
    font-size: 14.5px; letter-spacing: .6px; color: var(--ink-white);
    text-transform: uppercase;
  }
  .poster__visit a { color: var(--accent-red); text-decoration: none; }

  .sponsor-band {
    position: absolute; left: 0; right: 0; bottom: 0; height: 111px;
    background: var(--band);
    padding-top: 14px;
  }
  .sponsor-band__thanks {
    text-align: center;
    font-family: "Lora", serif; font-style: italic;
    font-size: 10.5px; color: var(--sponsor-blue);
  }
  .sponsor-band__list {
    display: flex; justify-content: space-around; align-items: center;
    margin-top: 24px; padding: 0 10px;
  }
  .sponsor {
    display: flex; align-items: center; gap: 5px;
    font-family: "Oswald", sans-serif; font-weight: 500;
    font-size: 12px; line-height: 1.05; text-transform: uppercase;
  }
  .sponsor__mark { width: 10px; height: 10px; flex: none; }
  .sponsor--tackle { color: #2d4a2a; }
  .sponsor--tackle .sponsor__mark { background: #d8b22a; }
  .sponsor--harlow { color: #a0262a; }
  .sponsor--harlow .sponsor__mark { background: #a0262a; border-radius: 50%; }
  .sponsor--bayview { color: var(--sponsor-grey); }
  .sponsor--bayview .sponsor__mark { background: #5a3f8a; }
  .sponsor--northgate { color: var(--sponsor-blue); }
  .sponsor--northgate .sponsor__mark { background: var(--sponsor-blue); border-radius: 50%; }
</style>
</head>
<body>
  <article class="poster">
    <div class="poster__photo" role="img" aria-label="Close-up photograph of a guitarist's hand on a guitar under purple and pink stage lights, with a decorative floral swirl ornament in the upper right"></div>

    <div class="event-badge">
      <span class="event-badge__dot"></span>
      <span class="event-badge__name">Riverside<br>Days</span>
    </div>

    <h1 class="poster__year">2019</h1>
    <h2 class="poster__title">Miraluna</h2>
    <p class="poster__subtitle">MUSIC &amp; ARTS FESTIVAL</p>

    <p class="poster__details">
      <span class="date">7–12 October</span>
      <span class="place">Green Cove Springs,</span>
      <span class="state">Florida</span>
    </p>

    <p class="poster__visit">For a complete shedule please visit <a href="#">miraluna.com</a></p>

    <footer class="sponsor-band">
      <p class="sponsor-band__thanks">Thank you to our Major Sponsors for their continuing support</p>
      <div class="sponsor-band__list">
        <span class="sponsor sponsor--tackle"><span class="sponsor__mark"></span>Crestline<br>Tackle</span>
        <span class="sponsor sponsor--harlow"><span class="sponsor__mark"></span>Harlow &amp;<br>Partners</span>
        <span class="sponsor sponsor--bayview"><span class="sponsor__mark"></span>Bayview<br>Health</span>
        <span class="sponsor sponsor--northgate"><span class="sponsor__mark"></span>Northgate<br>Credit Union</span>
      </div>
    </footer>
  </article>
</body>
</html>
```